Start-up incubator needs an informative marketing brochure

Birchwell Harbor Advisory is a start-up incubator helping entrepreneurs to develop their business in the Interactive Digital Media field, by working with a government grant under Creative Growth Bureau.
We got the content ready and would like the designer to match it with great design that is related to the brand, logo and scope of the content, and content positioning that brings about the ease of reading.
The end product should give the reader a good idea about our role as an incubator, and get the reader interested to find out more about the incubation program through our website.
We will use the flyer digitally, to send to interested parties to know more about our program, but we will also print some physical flyer out in A5 size.
Target Market(s)
Start-up entrepreneurs looking for help in finance or advisory
Industry/Entity Type
Marketing
Look and feel

```html
<!DOCTYPE html>
<html lang="en">
<head>
<meta charset="utf-8">
<title>Birchwell Harbor Incubation Program – Flyer</title>
<link rel="stylesheet" href="https://fonts.googleapis.com/css2?family=Cinzel:wght@600&family=Questrial&family=Montserrat:wght@700&display=swap">
<style>
  :root {
    --navy: #323d5a;
    --yellow: #f5b71b;
    --ink: #2b2f3a;
    --paper: #ffffff;
    --grid: #e6e9f0;
    --stage: #e4e6ea;
  }
  * { box-sizing: border-box; margin: 0; padding: 0; }
  html, body { width: 1200px; height: 1000px; overflow: hidden; background: var(--stage); }
  body { position: relative; font-family: "Questrial", "Century Gothic", sans-serif; color: var(--ink); }

  .page {
    position: absolute; top: 104px; width: 560px; height: 792px;
    background-color: var(--paper);
    background-image:
      linear-gradient(var(--grid) 1px, transparent 1px),
      linear-gradient(90deg, var(--grid) 1px, transparent 1px);
    background-size: 14px 14px;
    box-shadow: 0 2px 10px rgba(0,0,0,.15);
    overflow: hidden;
  }
  .page--front { left: 30px; }
  .page--back { left: 610px; }
  .page > * { position: absolute; }

  .header-band { top: 30px; left: 0; height: 80px; background: var(--navy); }
  .page--front .header-band { width: 390px; }
  .page--back .header-band { width: 340px; }
  .program-title {
    top: 42px; left: 40px; font-family: "Cinzel", serif; font-weight: 600;
    font-size: 23px; line-height: 1.25; color: #fff; letter-spacing: .5px;
  }
  .header-tab {
    top: 62px; right: 0; height: 56px; background: var(--yellow);
    display: flex; align-items: center; justify-content: center; gap: 8px;
    color: var(--navy);
  }
  .page--front .header-tab { width: 180px; }
  .page--back .header-tab { width: 230px; }
  .brand-name { font-family: "Cinzel", serif; font-weight: 600; font-size: 15px; }
  .brand-mark { width: 10px; height: 10px; background: var(--navy); }
  .tab-heading { font-family: "Montserrat", sans-serif; font-weight: 700; font-size: 21px; }

  .body-text { font-size: 12.5px; line-height: 1.45; }

  .bubble {
    border: 2px solid var(--navy); background: #fff;
    font-family: "Montserrat", sans-serif; font-weight: 700; font-size: 15px; line-height: 1.15;
    color: var(--navy); padding: 8px 10px; white-space: nowrap;
  }
  .bubble .accent { color: var(--yellow); }
  .bubble-tail { position: absolute; }
  .bubble .body-text { white-space: normal; font-weight: 400; }

  .check-list, .deal-list { list-style: none; }
  .check-list li { position: relative; padding-left: 16px; margin-bottom: 7px; font-size: 12.5px; line-height: 1.5; }
  .check-list li::before { content: "\2713"; position: absolute; left: 0; top: 0; color: var(--navy); font-weight: bold; }
  .deal-list li { position: relative; padding-left: 14px; font-size: 12px; line-height: 1.38; }
  .deal-list li::before { content: ""; position: absolute; left: 2px; top: 5px; border-left: 6px solid var(--navy); border-top: 3.5px solid transparent; border-bottom: 3.5px solid transparent; }

  .footer-band { left: 0; width: 560px; background: var(--navy); }
  .footer-strip { left: 0; width: 560px; background: var(--yellow); }
  .footer-note { color: #fff; font-style: italic; font-size: 14px; line-height: 1.35; text-align: center; }

  .alumni-quote { font-size: 12px; line-height: 1.45; }
  .alumni-tag {
    background: var(--yellow); color: var(--navy); font-size: 12.5px;
    padding: 3px 14px; font-weight: bold;
  }
  .unsure-box {
    background: var(--navy); font-family: "Montserrat", sans-serif; font-weight: 700;
    font-size: 26px; line-height: 1.1; color: #fff; padding: 16px 18px;
  }
  .unsure-box .accent { color: var(--yellow); }
  .web-note { font-size: 11.5px; }
  .web-address { font-size: 19px; color: var(--ink); }
</style>
</head>
<body>

<section class="page page--front">
  <div class="header-band"></div>
  <h1 class="program-title">Birchwell Harbor<br>Incubation Program</h1>
  <div class="header-tab"><span class="brand-mark"></span><span class="brand-name">Birchwell Harbor</span></div>

  <p class="body-text intro" style="top:130px;left:40px;width:490px;">
    Birchwell Harbor Advisory (BHA) aims to help build Information Communication Technology (ICT) into a major pillar of Singapore's economy. We are the sole appointed incubator of the i.SPARK Reload Grant which focuses on funding projects in the Interactive Digital Media (IDM) field.
  </p>

  <div class="bubble idm-bubble" style="top:222px;left:22px;">
    <span class="accent">WHAT PROJECTS</span><br>ARE CONSIDERED<br>IDM?
    <svg class="bubble-tail" style="right:20px;bottom:-13px;" width="16" height="13" viewBox="0 0 16 13"><path d="M0 0 L14 12 L12 0" fill="#fff" stroke="#323d5a" stroke-width="2"/></svg>
  </div>
  <p class="body-text" style="top:226px;left:200px;width:335px;">
    Any digital product in any industry vertical such as web, mobile and wearable applications that is designed for user interactions qualifies as IDM related.
  </p>

  <ul class="check-list" style="top:318px;left:30px;width:295px;">
    <li>I have an idea but don't know anything about starting a business</li>
    <li>I'm a hobby techie and I love building stuff, but I'm not sure how to commercialize them</li>
    <li>I have an idea for a product but don't have enough funds to build it</li>
    <li>I have an idea/product and have validated it through a start-up boot camp</li>
    <li>I have started my business and have gained some traction</li>
  </ul>

  <div class="bubble stage-box" style="top:350px;left:338px;width:198px;height:225px;text-align:center;">
    <svg class="bubble-tail" style="left:10px;bottom:-14px;" width="16" height="14" viewBox="0 0 16 14"><path d="M0 0 L2 13 L14 0" fill="#fff" stroke="#323d5a" stroke-width="2"/></svg>
    <span class="accent">WHAT STAGE</span><br>ARE YOU AT<br>RIGHT NOW<br>AT THIS POINT<br>IN TIME?
    <p class="body-text" style="font-family:'Questrial',sans-serif;font-size:11.5px;margin-top:14px;color:var(--ink);">
      Every stage requires a different approach to develop your business. BHA can lead you to the path that is right for you.
    </p>
  </div>

  <div class="bubble deal-bubble" style="top:610px;left:22px;width:118px;height:86px;padding-top:16px;">
    WHAT'S<br><span class="accent">THE</span> DEAL?
    <svg class="bubble-tail" style="right:-14px;top:10px;" width="14" height="16" viewBox="0 0 14 16"><path d="M0 0 L13 2 L0 14" fill="#fff" stroke="#323d5a" stroke-width="2"/></svg>
  </div>
  <ul class="deal-list" style="top:604px;left:156px;width:384px;">
    <li>i.SPARK S$50k development grant <strong>(no loss of equity)</strong></li>
    <li>Methodology of successful startup development</li>
    <li>Advisory from entrepreneurs with more than 15 years of experience</li>
    <li>Free incubation space</li>
    <li>Benefits from sponsors</li>
    <li>Syndicated follow-on funding for viable startups</li>
  </ul>

  <div class="footer-band" style="top:712px;height:62px;"></div>
  <p class="footer-note" style="top:720px;left:40px;width:480px;">
    Our efforts have resulted in 16 i.SPARK grants obtained, S$1.1m government grants approved, and another S$1.425m in follow-on funding.
  </p>
  <div class="footer-strip" style="top:774px;height:18px;"></div>
</section>

<section class="page page--back">
  <div class="header-band"></div>
  <h1 class="program-title">Birchwell Harbor<br>Incubation Program</h1>
  <div class="header-tab"><span class="tab-heading">INTERESTED?</span></div>

  <div class="bubble requirements-bubble" style="top:135px;left:30px;">
    <span class="accent">WE HAVE</span> SOME<br><span class="accent">REQUIREMENTS</span> FOR<br>OUR INCUBATEES:
    <svg class="bubble-tail" style="left:30px;bottom:-13px;" width="16" height="13" viewBox="0 0 16 13"><path d="M0 0 L2 12 L14 0" fill="#fff" stroke="#323d5a" stroke-width="2"/></svg>
  </div>

  <ul class="check-list" style="top:232px;left:40px;width:260px;">
    <li>2 full time founders</li>
    <li>Singaporean full time founder(s) owns more than 40% equity</li>
    <li>Business idea is related to Interactive Digital Media (IDM) field</li>
  </ul>

  <p class="body-text" style="top:350px;left:42px;width:245px;">
    If you meet the requirements, drop us a message immediately at our website (birchwellharboradvisory.sg) to discuss more about your venture. Don't hesitate as space is limited!
  </p>
  <p class="body-text" style="top:470px;left:42px;width:245px;">
    If you are unsure what your business needs, feel free to reach out to us as well, we are more than happy to give you our feedback.
  </p>

  <div class="bubble alumni-bubble" style="top:150px;left:322px;width:178px;text-align:center;">
    <span class="accent">HEAR WHAT</span><br>OUR ALUMNI<br>SAY ABOUT US:
    <svg class="bubble-tail" style="right:24px;bottom:-13px;" width="16" height="13" viewBox="0 0 16 13"><path d="M0 0 L14 12 L14 0" fill="#fff" stroke="#323d5a" stroke-width="2"/></svg>
  </div>

  <p class="alumni-quote" style="top:248px;left:322px;width:212px;">
    The mentors at Birchwell Harbor Advisory are really awesome. It is truly Entrepreneurs building Entrepreneurs. They have provided great support in our application for i.SPARK funding. Darren (our mentor) has been very patient and sincere in guiding us through the whole process. It is great having them as an incubator. Special thanks to the administrative support given by Farah.
  </p>
  <span class="alumni-tag" style="top:448px;right:26px;">TaskLane</span>

  <p class="alumni-quote" style="top:500px;left:322px;width:212px;">
    The i.SPARK scheme has helped Abacus Dojo founders kick start the vision of bringing Singapore math to life and fun to the children. The mentors in BHA have been very helpful in providing useful contacts and timely guidance to see the team through to commercialization and beyond.
  </p>
  <span class="alumni-tag" style="top:650px;right:26px;">Abacus Dojo</span>

  <div class="unsure-box" style="top:622px;left:30px;width:165px;">
    STILL<br><span class="accent">UNSURE?</span>
    <svg class="bubble-tail" style="right:-12px;top:14px;" width="12" height="16" viewBox="0 0 12 16"><path d="M0 0 L12 2 L0 14 Z" fill="#323d5a"/></svg>
  </div>
  <p class="web-note" style="top:676px;left:215px;width:320px;">Check out our website for FAQs and other information.</p>
  <p class="web-address" style="top:696px;left:215px;">Web: birchwellharboradvisory.sg</p>

  <div class="footer-band" style="top:742px;height:10px;"></div>
  <div class="footer-strip" style="top:752px;height:40px;"></div>
</section>

</body>
</html>
```